Vorumplex Bootcamp Schedule Flyer

***IMPORTANT: This flyer must be CS3 compatible and in layers so we can edit it. We have to be able to change times and details in photoshop***

This is for a 2 sided flyer with an attached .PSD template for specs (titled 4.25x5.5_14_Flyers). We need a flyer designed for our fitness bootcamp schedule with graphics, photos and info on both sides. Our company name is Vorumplex. We've included our previous schedule that we've been using but we want something better. Way better! DO NOT USE the previous schedule as a "design" template. We want a better for appealing design. Also we added a 5am session for Monday, Wednesday and Fridays. NO STOCK PHOTOS.

The first schedule designed the "CLOSED" is way too big (please do not make the closed too big or emphasized) and the days of the week are all different sized fonts and colors. Needs a lot of work.

On the other side we want something like the "Example Flyer" we attached but with the quote, "The Most Fun You'll Ever Have in a Gym While Getting In Shape" ***Please use the photo attached with the 3 women on the battle ropes for this side of the flyer*** The "Example Flyer" is not our company so don't use the company name on it.

Also we love the "Best In" logo (attached) but need it to say "Best Gym in Brighton 2015" with the rounded ink stamp look. We were Voted Best Gym in Brighton 2015 and would love that at the bottom of the flyer on the back side as well.

Please use the photos how you want for the flyer to look good. You don't have to use them but they are from our bootcamps.

We included photos, the old schedule, the example flyer for the back side and our logo.

Industry/Entity Type

Fitness

Requirements
Must have
• Must have Bootcamp logo, schedule, contact info at bottom, flyer design on back similar to attached "Example flyer"
Nice to have
• Great graphic similar to the screenshot attached of the "Best of" but have it say "Best Gym in Brighton 2015" in a round ink stamp type logo very similar to what we attached
Should not have
• Stock photos

```html
<!DOCTYPE html>
<html lang="en">
<head>
<meta charset="utf-8">
<title>Vorumplex Bootcamp Schedule Flyer</title>
<link href="https://fonts.googleapis.com/css2?family=Black+Ops+One&family=Roboto+Slab:wght@700&family=Oswald:wght@500;600&display=swap" rel="stylesheet">
<style>
  :root {
    --page-bg: #3a3a3a;
    --orange: #f47a1f;
    --orange-deep: #e0560c;
    --orange-light: #f9a04a;
    --ink: #111111;
    --asphalt: #1e1e1e;
    --white: #ffffff;
    --paper: #f1f1f1;
    --silver-top: #fbfbfb;
    --silver-bottom: #b9b9b9;
    --logo-blue: #3a8fd0;
  }
  * { margin: 0; padding: 0; box-sizing: border-box; }
  html, body { width: 1200px; height: 907px; overflow: hidden; background: var(--page-bg); }

  .flyer {
    position: absolute; left: 368px; top: 70px;
    width: 545px; height: 762px; overflow: hidden;
    background: var(--paper);
    box-shadow: 0 6px 18px rgba(0,0,0,.5);
  }
  .flyer__bands { position: absolute; left: 0; top: 0; }

  .photo { position: absolute; }
  .photo--runner {
    left: 360px; top: 20px; width: 185px; height: 540px;
    background: linear-gradient(180deg, rgba(236,150,120,.7) 0%, rgba(70,60,70,.85) 50%, rgba(25,25,28,.95) 100%);
  }
  .photo--pushup {
    left: 0; top: 576px; width: 250px; height: 186px;
    background: linear-gradient(160deg, #6a6a6a 0%, #3a3a3a 60%, #b04a5a 100%);
  }

  .brand {
    position: absolute; left: 48px; top: 26px; width: 247px; height: 76px;
    background: var(--white); border: 3px solid var(--ink); border-radius: 6px;
    display: flex; align-items: center; justify-content: center; gap: 10px;
  }
  .brand__mark { width: 14px; height: 14px; background: var(--logo-blue); }
  .brand__name { font-family: "Black Ops One", sans-serif; font-size: 30px; color: var(--logo-blue); }

  .headline {
    position: absolute; left: 40px; top: 118px; width: 270px; text-align: center;
    font-family: "Black Ops One", sans-serif; font-weight: 400; line-height: 1;
  }
  .headline__main { font-size: 54px; color: var(--ink); }
  .headline__sub { font-size: 42px; color: var(--white); margin-top: 6px; }

  .schedule-text {
    font-family: "Roboto Slab", serif; font-weight: 700;
    font-size: 14px; line-height: 20px; text-align: center;
  }
  .weekday-times { position: absolute; left: 30px; top: 280px; width: 290px; color: var(--ink); }

  .early-session { position: absolute; left: 40px; top: 345px; width: 290px; height: 104px; }
  .early-session svg { position: absolute; left: 0; top: 0; }
  .early-session__text {
    position: absolute; left: 0; top: 28px; width: 290px; text-align: center; color: var(--ink);
  }
  .early-session__line1 { font-family: "Roboto Slab", serif; font-weight: 700; font-size: 13px; }
  .early-session__line1 b { font-size: 24px; }
  .early-session__line2 { font-family: "Oswald", sans-serif; font-weight: 600; font-size: 23px; line-height: 28px; }

  .weekend { position: absolute; left: 30px; top: 460px; width: 290px; color: var(--white); }
  .closed {
    position: absolute; left: 30px; top: 508px; width: 290px; text-align: center;
    font-family: "Black Ops One", sans-serif; font-size: 42px; line-height: 1; color: var(--orange);
  }
  .details {
    position: absolute; left: 262px; top: 590px; width: 270px;
    font-family: "Oswald", sans-serif; font-weight: 500;
    font-size: 13px; line-height: 23px; color: var(--white);
  }
  .contact {
    position: absolute; right: 28px; top: 704px;
    font-family: "Black Ops One", sans-serif; font-size: 24px; line-height: 1;
    color: var(--ink); white-space: nowrap;
  }
</style>
</head>
<body>
  <main class="flyer">
    <svg class="flyer__bands" width="545" height="762" viewBox="0 0 545 762">
      <defs>
        <linearGradient id="orangeField" x1="0" y1="0" x2="1" y2="1">
          <stop offset="0" stop-color="#e0560c"/>
          <stop offset=".5" stop-color="#f47a1f"/>
          <stop offset="1" stop-color="#f9a04a"/>
        </linearGradient>
      </defs>
      <rect class="band-orange" width="545" height="375" fill="url(#orangeField)"/>
      <polygon class="band-tear-top" fill="#ffffff"
        points="0,355 40,362 70,350 120,366 180,352 250,368 320,356 400,372 460,360 545,374 545,395 0,395"/>
      <polygon class="band-asphalt" fill="#1e1e1e"
        points="0,378 60,372 130,384 200,374 280,386 360,376 440,388 545,380 545,690 470,676 400,684 330,670 260,682 180,668 100,680 0,672"/>
    </svg>

    <div class="photo photo--runner" role="img" aria-label="Photo of a woman running in workout clothes"></div>

    <div class="brand">
      <span class="brand__mark"></span>
      <span class="brand__name">VORUMPLEX</span>
    </div>

    <h1 class="headline">
      <div class="headline__main">FITNESS</div>
      <div class="headline__sub">BOOTCAMP</div>
      <div class="headline__sub">SCHEDULE</div>
    </h1>

    <p class="weekday-times schedule-text">MONDAY- FRIDAY<br>6AM, 8.30AM, NOON, 4.30PM<br>5.30PM, 6.30PM</p>

    <div class="early-session">
      <svg width="290" height="104" viewBox="0 0 290 104">
        <defs>
          <linearGradient id="silver" x1="0" y1="0" x2="0" y2="1">
            <stop offset="0" stop-color="#fbfbfb"/>
            <stop offset="1" stop-color="#b9b9b9"/>
          </linearGradient>
        </defs>
        <path d="M6 14 L280 2 Q288 2 288 10 L286 92 Q286 100 278 100 L10 102 Q2 102 2 94 L0 22 Q0 14 6 14 Z"
          fill="url(#silver)" stroke="#888" stroke-width="1"/>
      </svg>
      <div class="early-session__text">
        <div class="early-session__line1"><b>5AM</b> SESSION FOR MONDAY</div>
        <div class="early-session__line2">WEDNESDAY AND FRIDAYS</div>
      </div>
    </div>

    <p class="weekend schedule-text">SATURDAY 9AM<br>SUNDAY AND MAJOR HOLIDAYS</p>
    <p class="closed">CLOSED</p>

    <p class="details">TOTAL BODY TRANSFORMATION WORKOUT<br>ALL BOOTCAMPS ARE 50 MINUTES IN LENGTH</p>

    <svg class="flyer__bands" width="545" height="762" viewBox="0 0 545 762">
      <polygon class="band-tear-bottom" fill="#f1f1f1"
        points="0,672 100,680 180,668 260,682 330,670 400,684 470,676 545,690 545,762 0,762"/>
    </svg>

    <div class="photo photo--pushup" role="img" aria-label="Photo of a man doing push-ups on kettlebells"></div>

    <p class="contact">CALL 303-555-0172</p>
  </main>
</body>
</html>
```